Specialized Personal Trainer Needs a Business Card Design

I need a business card design for my personal training business called Tall Oak Fitness. I have my Human Kinetics degree in Exercise Science from the Halvern Ridge University as well as an extra certification from NBEP (National Board of Exercise Practice). I work as a Cardiac Rehab Exercise Specialist and personal trainer giving specialized exercise prescriptions to those that have different heart conditions as well as work with the general population in weight loss, strength and conditioning, getting/staying fit.
Updates

I decided that I wanted a logo (as I did not have one before I submitted my project for a business card) so I am submitting a project to get a logo done and then I will decide on a business card, hopefully being able to use one of the designs already submitted.  My apologies for doing this backwards.  I am new to this so I appreciate your patience.

Thank you.

Hi, I have just created a project for a logo design (I realized I needed a logo and I should've done that first..oops!), please feel free to participate.  Once I receive a logo I like I will finalize my business card project and hopefully incorporate it into one of your business card designs. 

Thank you!

Target Market(s)

Business professionals

Industry/Entity Type

Personal Trainer

Requirements
Must have
• My name with my info:
Celia R. Dunhill (BHK)
NBEP Certified Clinical Exercise Specialist & Personal Trainer
celia.dunhill@talloakfitness.example
Cell: 604-358-4170

Please make it double sided.
Nice to have
• An image that represents cardiac and general fitness training.

```html
<!DOCTYPE html>
<html lang="en">
<head>
<meta charset="utf-8">
<title>Tall Oak Fitness – Business Card</title>
<link rel="stylesheet" href="https://fonts.googleapis.com/css2?family=Open+Sans:ital,wght@0,400;0,700;1,400&display=swap">
<style>
  :root {
    --page-bg: #2c3f8f;
    --navy-deep: #062a6e;
    --navy: #0a47a8;
    --blue: #1673d6;
    --cyan: #1fc6ef;
    --cyan-light: #5fe3ff;
    --ice: #d6f7ff;
    --glow: #bff4ff;
    --ink: #0b2f9c;
    --shadow: rgba(0, 10, 40, 0.45);
  }
  html, body {
    margin: 0;
    width: 1200px;
    height: 900px;
    overflow: hidden;
    background: var(--page-bg);
  }
  .sheet {
    position: relative;
    width: 1200px;
    height: 900px;
  }
  .card {
    position: absolute;
    left: 250px;
    width: 700px;
    height: 400px;
    box-shadow: 0 14px 30px var(--shadow);
  }
  .card--brand { top: 40px; }
  .card--contact { top: 465px; }
  .card svg { display: block; width: 700px; height: 400px; }

  .wordmark {
    font-family: "Open Sans", sans-serif;
    font-weight: 700;
    fill: var(--ice);
  }
  .holder-name {
    font-family: "Open Sans", sans-serif;
    font-size: 27px;
    fill: var(--ink);
  }
  .holder-title {
    font-family: "Open Sans", sans-serif;
    font-style: italic;
    font-size: 16.5px;
    fill: var(--ink);
  }
  .holder-contact {
    font-family: "Open Sans", sans-serif;
    font-style: italic;
    font-size: 17px;
    fill: var(--ink);
  }
  .pulse-line { stroke: var(--glow); stroke-width: 3; fill: none; }
  .pulse-glow { stroke: var(--cyan-light); stroke-width: 10; fill: none; opacity: 0.55; }
  .logo-band { fill: var(--navy-deep); opacity: 0.85; }
  .wave-band { fill: var(--navy-deep); }
  .wave-mid { fill: var(--navy); }
  .wave-edge { fill: var(--cyan); opacity: 0.9; }
</style>
</head>
<body>
<main class="sheet">

  <!-- Brand side -->
  <section class="card card--brand" aria-label="Business card, brand side">
    <svg viewBox="0 0 700 400" xmlns="http://www.w3.org/2000/svg">
      <defs>
        <linearGradient id="brandBg" x1="0" y1="1" x2="1" y2="0">
          <stop offset="0" style="stop-color:var(--cyan)"/>
          <stop offset="0.45" style="stop-color:var(--blue)"/>
          <stop offset="1" style="stop-color:var(--navy-deep)"/>
        </linearGradient>
        <linearGradient id="helixFade" x1="0" y1="0" x2="1" y2="0">
          <stop offset="0" style="stop-color:var(--navy)" stop-opacity="0"/>
          <stop offset="1" style="stop-color:var(--navy-deep)" stop-opacity="0.6"/>
        </linearGradient>
        <filter id="softGlow" x="-10%" y="-200%" width="120%" height="500%">
          <feGaussianBlur stdDeviation="4"/>
        </filter>
      </defs>
      <rect width="700" height="400" fill="url(#brandBg)"/>
      <rect class="helix-art" x="380" y="40" width="320" height="220" fill="url(#helixFade)"
            role="img" aria-label="Faint double-helix illustration in the background"/>
      <line class="pulse-glow" x1="0" y1="62" x2="700" y2="62" filter="url(#softGlow)"/>
      <line class="pulse-line" x1="0" y1="62" x2="700" y2="62"/>
      <path class="logo-band" d="M40 150 H520 L550 180 H700 V260 H40 Z"/>
      <text class="wordmark" x="350" y="225" font-size="60" text-anchor="middle">Tall Oak Fitness</text>
      <line class="pulse-glow" x1="0" y1="318" x2="700" y2="318" filter="url(#softGlow)"/>
      <line class="pulse-line" x1="0" y1="318" x2="700" y2="318"/>
    </svg>
  </section>

  <!-- Contact side -->
  <section class="card card--contact" aria-label="Business card, contact side">
    <svg viewBox="0 0 700 400" xmlns="http://www.w3.org/2000/svg">
      <defs>
        <linearGradient id="contactBg" x1="0" y1="1" x2="0.6" y2="0">
          <stop offset="0" style="stop-color:var(--cyan-light)"/>
          <stop offset="0.5" style="stop-color:var(--cyan)"/>
          <stop offset="1" style="stop-color:var(--navy)"/>
        </linearGradient>
        <linearGradient id="runnerTone" x1="0" y1="0" x2="1" y2="1">
          <stop offset="0" style="stop-color:var(--ice)" stop-opacity="0.55"/>
          <stop offset="1" style="stop-color:var(--cyan-light)" stop-opacity="0.35"/>
        </linearGradient>
        <radialGradient id="watchTone" cx="0.5" cy="0.5" r="0.5">
          <stop offset="0" style="stop-color:var(--ice)" stop-opacity="0.25"/>
          <stop offset="1" style="stop-color:var(--ice)" stop-opacity="0"/>
        </radialGradient>
        <linearGradient id="waveTone" x1="0" y1="0" x2="1" y2="0">
          <stop offset="0" style="stop-color:var(--navy-deep)"/>
          <stop offset="1" style="stop-color:var(--navy)"/>
        </linearGradient>
        <filter id="softGlow2" x="-10%" y="-200%" width="120%" height="500%">
          <feGaussianBlur stdDeviation="4"/>
        </filter>
      </defs>
      <rect width="700" height="400" fill="url(#contactBg)"/>
      <rect class="runner-art" x="600" y="8" width="86" height="82" rx="10" fill="url(#runnerTone)"
            role="img" aria-label="Silhouette of a sprinting runner"/>
      <rect class="stopwatch-art" x="555" y="165" width="140" height="150" fill="url(#watchTone)"
            role="img" aria-label="Faint stopwatch illustration"/>
      <line class="pulse-glow" x1="0" y1="96" x2="600" y2="96" filter="url(#softGlow2)"/>
      <line class="pulse-line" x1="0" y1="96" x2="600" y2="96"/>
      <text class="wordmark" x="250" y="158" font-size="44">Tall Oak Fitness</text>

      <text class="holder-name" x="72" y="228">Celia R. Dunhill (BHK)</text>
      <text class="holder-title" x="78" y="262">NBEP Certified Clinical Exercise Specialist &amp; Personal Trainer</text>
      <text class="holder-contact" x="70" y="294">celia.dunhill@talloakfitness.example</text>
      <text class="holder-contact" x="62" y="324">Cel: 604-358-4170</text>

      <path class="wave-edge" d="M0 345 C160 300 330 395 520 360 C600 345 660 330 700 325 V400 H0 Z"/>
      <path d="M0 352 C160 310 330 405 520 370 C600 355 660 340 700 335 V400 H0 Z" fill="url(#waveTone)"/>
    </svg>
  </section>

</main>
</body>
</html>
```